Kobalto Cell Phone Repair

We are a small cell phone repair store in need of a redesign to our current business card to make it a more modern, cleaner design that will catch folks' attention (perhaps with rounded edges ) - But still include most of the information listed on the current card. Would like to keep the current color scheme of black/white and green. Card will not need any personnel name included. Would like to see some designs include takes on a velorin or tekvo screen as well as more traditional cards.

Target Market(s)

broad spectrum across all cell phone users

Industry/Entity Type

Cell Phone

Contact Information for Business Card

changes to front text:
keep business Logo
business address, phone number website and email. All other info optional (add gathernest and blurvo icons on card

Rear of card:

Keep repair services, change tekvo repair to slatra repair, change quorvex os repair to data recovery (with appropriate icon or substitute)
remove products text
remove pjw and ravesh from manufacturer logos, add dunbelio.

Requirements
Must have
• business Logo
• business address, phone number website and email
• keep colors to white/black/green/gray
• gathernest and blurvo icons on card
Nice to have
• Would like to see 'traditional' business card design as well as creative design incorporating incorporating front of cell phone (eg tekvo or quorvex). Rounded edges would be nice but not necessary.

```html
<!DOCTYPE html>
<html lang="en">
<head>
<meta charset="utf-8">
<title>Kobalto Cell Phone Repair – Business Card</title>
<link rel="stylesheet" href="https://fonts.googleapis.com/css2?family=Josefin+Sans:wght@700&display=swap">
<style>
  :root {
    --paper: #ffffff;
    --frame: #4b4b4d;
    --ink: #111111;
    --green: #5cb443;
    --teal: #1ba9c6;
    --social-blue: #4a67a8;
    --mark: #000000;
    --trim: #d8d8d8;
  }
  * { margin: 0; padding: 0; box-sizing: border-box; }
  html, body { width: 1200px; height: 804px; overflow: hidden; background: var(--paper); }
  .sheet { position: relative; width: 1200px; height: 804px; }
  .print-marks { position: absolute; inset: 0; }

  .card-frame {
    position: absolute; left: 78px; top: 86px; width: 1044px; height: 628px;
    background: var(--frame); border-radius: 72px;
  }
  .card-face {
    position: absolute; left: 142px; top: 118px; width: 916px; height: 560px;
    background: var(--paper); border-radius: 62px;
  }

  /* text blocks run bottom-to-top; left/top give the block centre */
  .rotated {
    position: absolute; white-space: nowrap; text-align: center;
    transform: translate(-50%, -50%) rotate(-90deg);
    font-family: "Josefin Sans", sans-serif; font-weight: 700;
  }

  .brand-block { left: 345px; top: 335px; color: var(--ink); }
  .brand-name { display: block; font-size: 74px; line-height: 84px; letter-spacing: 2px; }
  .brand-tagline { display: block; font-size: 30px; line-height: 40px; }
  .brand-dot {
    position: absolute; left: 286px; top: 500px; width: 116px; height: 116px;
    border-radius: 50%; background: var(--green);
  }

  .address { left: 640px; top: 405px; font-size: 28px; line-height: 38px; color: var(--ink); }
  .contact { left: 743px; top: 388px; font-size: 28px; line-height: 34px; color: var(--green); }
  .contact-line { display: inline-flex; align-items: center; gap: 10px; }
  .contact-line svg { width: 22px; height: 22px; }
  .social { left: 838px; top: 400px; font-size: 24px; line-height: 40px; }
  .social-gathernest { color: var(--social-blue); margin-right: 26px; }
  .social-blurvo { color: var(--teal); }
  .website { left: 908px; top: 400px; font-size: 30px; line-height: 34px; color: var(--ink); }
</style>
</head>
<body>
<div class="sheet">
  <svg class="print-marks" width="1200" height="804" viewBox="0 0 1200 804" aria-hidden="true">
    <rect x="78" y="86" width="1044" height="628" fill="none" stroke="var(--trim)" stroke-width="1"/>
    <g stroke="var(--mark)" stroke-width="1">
      <line x1="115" y1="15" x2="115" y2="75"/><line x1="1085" y1="15" x2="1085" y2="75"/>
      <line x1="115" y1="725" x2="115" y2="790"/><line x1="1085" y1="725" x2="1085" y2="790"/>
      <line x1="5" y1="122" x2="70" y2="122"/><line x1="1130" y1="122" x2="1195" y2="122"/>
      <line x1="5" y1="678" x2="70" y2="678"/><line x1="1130" y1="678" x2="1195" y2="678"/>
    </g>
    <defs>
      <g id="registration">
        <line x1="-52" y1="0" x2="52" y2="0" stroke="var(--mark)"/>
        <line x1="0" y1="-26" x2="0" y2="26" stroke="var(--mark)"/>
        <circle r="15" fill="none" stroke="var(--mark)" stroke-width="1.5"/>
        <circle r="10" fill="var(--mark)"/>
        <line x1="-7" y1="-7" x2="7" y2="7" stroke="#fff" stroke-width="2"/>
        <line x1="-7" y1="7" x2="7" y2="-7" stroke="#fff" stroke-width="2"/>
      </g>
    </defs>
    <use href="#registration" x="597" y="31"/>
    <use href="#registration" x="597" y="770"/>
    <use href="#registration" x="30" y="400" transform="rotate(90 30 400)"/>
    <use href="#registration" x="1166" y="400" transform="rotate(90 1166 400)"/>
  </svg>

  <div class="card-frame"></div>
  <div class="card-face"></div>

  <div class="brand-dot"></div>
  <div class="rotated brand-block">
    <span class="brand-name">KOBALTO</span>
    <span class="brand-tagline">CELL PHONE REPAIR</span>
  </div>

  <div class="rotated address">4870 Harbor Lane,<br>Brookfield MD 21987</div>

  <div class="rotated contact">
    <span class="contact-line">
      <svg viewBox="0 0 24 24" aria-hidden="true"><path fill="var(--green)" d="M6.6 10.8a15 15 0 0 0 6.6 6.6l2.2-2.2c.3-.3.7-.4 1-.2 1.1.4 2.3.6 3.6.6.6 0 1 .4 1 1V20c0 .6-.4 1-1 1A17 17 0 0 1 3 4c0-.6.4-1 1-1h3.5c.6 0 1 .4 1 1 0 1.3.2 2.5.6 3.6.1.3 0 .7-.2 1z"/></svg>
      555.013.2468
    </span><br>
    <span class="contact-line">
      <svg viewBox="0 0 24 24" aria-hidden="true"><rect x="2.5" y="5" width="19" height="14" fill="none" stroke="var(--green)" stroke-width="2"/><path d="M3 6l9 7 9-7" fill="none" stroke="var(--green)" stroke-width="2"/></svg>
      info@kobalto.com
    </span>
  </div>

  <div class="rotated social">
    <span class="social-gathernest">gathernest</span><span class="social-blurvo">blurvo</span>
  </div>

  <div class="rotated website">www.kobaltostore.com</div>
</div>
</body>
</html>
```